Tattoostudio
Zielgruppe
Tattoostudio, Junge Leute, Kreativ,
Aufgabenstellung
Visitenkarten mit vorhandenem Logo, hochkant, 2 Seitig, Vorderseite Logo + Studioname (Morgenfalke Tattoo) Rückseite mit Kontaktdaten ( Artist/Inhaber, Facebook: facebook.com/MorgenfalkeTattoo

```html
<!DOCTYPE html>
<html lang="de">
<head>
<meta charset="utf-8">
<title>Morgenfalke Tattoo – Visitenkarten</title>
<link href="https://fonts.googleapis.com/css2?family=Courgette&display=swap" rel="stylesheet">
<style>
  :root {
    --stage: #3b3b3b;
    --card-dark: #141414;
    --card-mid: #262626;
    --card-edge: #4a4a4a;
    --mint: #3fd89a;
    --white: #f4f4f4;
    --art-pink: #d8346f;
    --art-violet: #6b4fb8;
    --art-teal: #2fb89a;
    --art-skin: #e8b79a;
  }
  * { margin: 0; padding: 0; box-sizing: border-box; }
  html, body { width: 1200px; height: 916px; overflow: hidden; }
  body {
    background: var(--stage);
    position: relative;
    font-family: "Courgette", cursive;
  }
  .card {
    position: absolute;
    top: 115px;
    width: 459px;
    height: 685px;
    background:
      radial-gradient(ellipse at 30% 25%, rgba(255,255,255,0.06), transparent 60%),
      radial-gradient(ellipse at 75% 80%, rgba(255,255,255,0.05), transparent 55%),
      linear-gradient(160deg, var(--card-mid), var(--card-dark));
    box-shadow: 0 0 0 1px var(--card-edge), 0 0 18px rgba(0,0,0,0.6);
    overflow: hidden;
  }
  .card--front { left: 101px; }
  .card--back { left: 640px; }

  .mascot-art {
    position: absolute;
    left: 75px; top: 60px;
    width: 300px; height: 400px;
    border-radius: 46% 46% 30% 30%;
    background:
      radial-gradient(circle at 30% 18%, var(--art-pink) 0 22%, transparent 40%),
      radial-gradient(circle at 70% 35%, var(--art-teal) 0 18%, transparent 42%),
      radial-gradient(circle at 55% 60%, var(--art-skin) 0 22%, transparent 45%),
      linear-gradient(180deg, var(--art-violet), #3a2a66);
    opacity: 0.9;
  }
  .studio-name {
    position: absolute;
    left: 0; right: 0; top: 470px;
    text-align: center;
    color: var(--mint);
    font-size: 60px;
    line-height: 1.05;
  }

  .contact {
    position: absolute;
    inset: 0;
    text-align: center;
    color: var(--white);
  }
  .divider {
    position: absolute;
    left: 129px;
    width: 200px;
    height: 14px;
  }
  .divider--top { top: 75px; }
  .divider--bottom { top: 594px; }
  .line {
    position: absolute;
    left: 0; right: 0;
    line-height: 1;
    white-space: nowrap;
  }
  .label { color: var(--mint); font-size: 23px; }
  .owner-name { font-size: 38px; }
  .detail { font-size: 27px; }
  .detail--small { font-size: 23px; }
</style>
</head>
<body>
  <section class="card card--front" aria-label="Vorderseite">
    <div class="mascot-art" role="img" aria-label="Illustration: Tätowiererin mit bunten Haaren, Blume im Haar und Tattoomaschine in der Hand"></div>
    <p class="studio-name">Morgenfalke<br>Tattoo</p>
  </section>

  <section class="card card--back" aria-label="Rückseite">
    <div class="contact">
      <svg class="divider divider--top" viewBox="0 0 200 14" aria-hidden="true">
        <line x1="0" y1="7" x2="200" y2="7" stroke="#f4f4f4" stroke-width="1.2"/>
        <path d="M88 7 Q100 -1 112 7 Q100 15 88 7 Z" fill="#f4f4f4"/>
      </svg>
      <p class="line label" style="top:114px">Artist/Inhaber:</p>
      <p class="line owner-name" style="top:150px">Lena Brandauer</p>
      <p class="line detail" style="top:198px">Lindenweg 8</p>
      <p class="line detail" style="top:238px">07745 Talhausen</p>
      <p class="line label" style="top:304px">Telefon</p>
      <p class="line detail" style="top:340px">0170 / 5521984</p>
      <p class="line label" style="top:405px">Email</p>
      <p class="line detail--small line" style="top:444px">MorgenfalkeTattoo@postfach-mail.de</p>
      <p class="line label" style="top:506px">Facebook</p>
      <p class="line detail--small line" style="top:546px">facebook.com/MorgenfalkeTattoo</p>
      <svg class="divider divider--bottom" viewBox="0 0 200 14" aria-hidden="true">
        <line x1="0" y1="7" x2="200" y2="7" stroke="#f4f4f4" stroke-width="1.2"/>
        <path d="M88 7 Q100 -1 112 7 Q100 15 88 7 Z" fill="#f4f4f4"/>
      </svg>
    </div>
  </section>
</body>
</html>
```